Wine Label for a Prosecco Wine Called Vuro

Prosecco is a white sparkling wine from Italy. We are looking for an eye catching, elegant label for this prosecco that is called "Vuro" because it is a young, fresh, lively white sparkling wine. (We do not want to see children or babies featured on the label-- just the name VURO please.) Attached is the old label for your reference, and the bottle type that will be used , which is a dark green Burgundy style bottle (pls ignore the label on the bottle). Please no grapes or wine glasses on the label. We are looking for something: eye catching / fun / ELEGANT (not cheap). We would be happy with a fun color too. Remember-- elegant, eye catching! Thanks!
Updates

Hi All, I think I made a mistake in my brief and have updated it. I also uploaded a competitor's label that we like very much to give better direction to what we are looking for. Also, the word Vuro cannot be vertical, nor can it be broken. It needs to read: VURO or Vuro. Thanks

Target Market(s)

American adults male and female.

Colors
abd036
33a6d7
33b8a4
ffcf3e

Requirements
Must have
• The mandatory information as shown on old labels. The word VURO should be very prominent.
Nice to have
• The uploaded photo of a competitor's prosecco shows a label we really like... if you could play around with this shape and style we'd be very happy.
Should not have
• No grape images, no wine glass images, no images of babies or children.

```html
<!DOCTYPE html>
<html lang="en">
<head>
<meta charset="utf-8">
<title>Vuro Prosecco Label</title>
<link href="https://fonts.googleapis.com/css2?family=Playfair+Display:wght@900&family=Tinos:wght@400&display=swap" rel="stylesheet">
<style>
  :root {
    --backdrop: #ffffff;
    --paper: #f6eed8;
    --ink: #4a3826;
    --ink-soft: #7a6548;
    --art-light: #f3e6c4;
    --art-dark: #b49a6c;
    --lime: #abd036;
    --sky: #33a6d7;
    --teal: #33b8a4;
    --sun: #ffcf3e;
  }
  * { margin: 0; padding: 0; box-sizing: border-box; }
  html, body {
    width: 682px; height: 1200px; overflow: hidden;
    background: var(--backdrop);
  }
  .canvas { position: relative; width: 682px; height: 1200px; }
  .label {
    position: absolute; left: 61px; top: 133px;
    width: 560px; height: 934px;
    background: var(--paper);
    border-radius: 18px;
  }
  .label-frame { position: absolute; inset: 0; }
  .crest-art {
    position: absolute; left: 110px; top: 48px;
    width: 340px; height: 380px;
    border-radius: 170px 170px 40px 40px;
    background: radial-gradient(circle at 50% 40%, var(--sun) 0%, var(--art-light) 38%, var(--art-dark) 100%);
    opacity: 0.9;
  }
  .name {
    position: absolute; left: 0; right: 0; top: 478px;
    text-align: center;
    font-family: "Playfair Display", serif; font-weight: 900;
    font-size: 112px; letter-spacing: 6px; line-height: 1;
    color: var(--ink);
  }
  .flourish {
    position: absolute; left: 140px; top: 612px;
    width: 280px; height: 34px;
    border-radius: 17px;
    background: linear-gradient(90deg, transparent, var(--teal) 20%, var(--sky) 50%, var(--teal) 80%, transparent);
    opacity: 0.6;
  }
  .description {
    position: absolute; left: 0; right: 0; top: 668px;
    text-align: center;
    font-family: "Tinos", serif; font-size: 26px; line-height: 1.3;
    color: var(--ink);
  }
  .volume, .strength {
    position: absolute; top: 736px;
    font-family: "Tinos", serif; font-size: 26px; line-height: 1.3;
    color: var(--ink);
  }
  .volume { left: 48px; }
  .strength { right: 48px; }
  .base-ornament {
    position: absolute; left: 60px; top: 826px;
    width: 440px; height: 60px;
    border-radius: 30px;
    background: linear-gradient(90deg, transparent, var(--art-dark) 25%, var(--art-dark) 75%, transparent);
    opacity: 0.5;
  }
</style>
</head>
<body>
<main class="canvas">
  <section class="label">
    <svg class="label-frame" width="560" height="934" viewBox="0 0 560 934" aria-hidden="true">
      <defs>
        <linearGradient id="brand-band" x1="0" y1="0" x2="1" y2="1">
          <stop offset="0" stop-color="var(--lime)"/>
          <stop offset="0.35" stop-color="var(--teal)"/>
          <stop offset="0.7" stop-color="var(--sky)"/>
          <stop offset="1" stop-color="var(--sun)"/>
        </linearGradient>
      </defs>
      <rect x="8" y="8" width="544" height="918" rx="14" fill="none" stroke="url(#brand-band)" stroke-width="6"/>
      <rect x="20" y="20" width="520" height="894" rx="10" fill="none" stroke="var(--ink)" stroke-width="2"/>
      <line x1="20" y1="456" x2="540" y2="456" stroke="var(--ink)" stroke-width="2.5"/>
      <line x1="20" y1="463" x2="540" y2="463" stroke="var(--sun)" stroke-width="3"/>
    </svg>
    <div class="crest-art" role="img" aria-label="Engraved-style crest illustration with sunburst and scrolls"></div>
    <h1 class="name">VURO</h1>
    <div class="flourish" role="img" aria-label="Ornamental scroll divider"></div>
    <p class="description">Prosecco is a white<br>sparkling wine<br>from Italy</p>
    <span class="volume">0,7 l</span>
    <span class="strength">12%</span>
    <div class="base-ornament" role="img" aria-label="Ornamental scrollwork border"></div>
  </section>
</main>
</body>
</html>
```